Bref créative
see logo info from logo info
Bluefern Trading Partners, Ltd.
Use same font as used in my logo
can also give other font suggestions
Modern
Daniel Okafor
President
742 Hollis St. - Suite 0830
New York, NY 10093
212-555-0147 Ext-305
sales@bluefernexample.com
bluefernexample.com
we are looking for business card and stationary design layouts.
logo with name
This is our logo to be used for the layout of the business cards and stationary.

```html
<!DOCTYPE html>
<html lang="en">
<head>
<meta charset="utf-8">
<title>Bluefern Trading Partners, Ltd. — Business Card</title>
<link rel="stylesheet" href="https://fonts.googleapis.com/css2?family=Tinos:wght@400;700&display=swap">
<style>
  :root {
    --backdrop: #2b2c2e;
    --card: #f7f7f8;
    --card-edge: #e3e4e6;
    --brand-blue: #1f5aa6;
    --ink: #3a3d42;
    --rule: #2a3b55;
  }
  * { margin: 0; padding: 0; box-sizing: border-box; }
  html, body {
    width: 1200px; height: 901px; overflow: hidden;
    background: var(--backdrop);
    font-family: "Tinos", "Times New Roman", serif;
  }
  .canvas {
    position: relative; width: 1200px; height: 901px;
    display: flex; flex-direction: column; align-items: center; justify-content: center; gap: 40px;
  }
  .card {
    position: relative; width: 700px; height: 400px;
    background: linear-gradient(160deg, #ffffff 0%, var(--card) 60%, var(--card-edge) 100%);
    border-radius: 22px;
    box-shadow: 0 14px 30px rgba(0,0,0,.45);
  }
  /* back side */
  .card-back .brand {
    position: absolute; left: 0; right: 0; top: 140px;
    display: flex; flex-direction: column; align-items: center; gap: 18px;
  }
  .brand-dot {
    width: 64px; height: 64px; border-radius: 50%; background: var(--brand-blue);
  }
  .brand-name {
    color: var(--brand-blue); font-weight: 700; text-transform: uppercase;
    letter-spacing: .5px; line-height: 1.05; text-align: center;
  }
  .card-back .brand-name { font-size: 26px; }
  .card-back .web {
    position: absolute; left: 40px; bottom: 30px;
    font-size: 17px; color: var(--ink);
  }
  /* front side */
  .card-front .brand {
    position: absolute; left: 30px; top: 120px; width: 300px;
    display: flex; flex-direction: column; align-items: center; gap: 14px;
  }
  .card-front .brand-dot { width: 56px; height: 56px; }
  .card-front .brand-name { font-size: 24px; }
  .divider {
    position: absolute; left: 352px; top: 70px; width: 2px; height: 220px;
    background: var(--rule);
  }
  .contact {
    position: absolute; left: 378px; top: 72px; color: var(--ink); font-size: 17px; line-height: 1.28;
  }
  .contact .person { color: var(--brand-blue); font-weight: 700; font-size: 25px; line-height: 1.1; }
  .contact .role { font-size: 16px; margin-bottom: 22px; }
  .contact .address { margin-bottom: 10px; }
  .contact .line { display: flex; align-items: center; gap: 8px; }
  .contact .icon { width: 14px; height: 14px; fill: var(--ink); flex: none; }
  .contact .plain { padding-left: 22px; }
  .card-front .web {
    position: absolute; left: 378px; top: 310px; font-size: 18px; color: var(--ink);
  }
</style>
</head>
<body>
<main class="canvas">
  <section class="card card-back" aria-label="Card back">
    <div class="brand">
      <span class="brand-dot"></span>
      <div class="brand-name">Bluefern Trading<br>Partners, Ltd.</div>
    </div>
    <div class="web">www.bluefernexample.com</div>
  </section>

  <section class="card card-front" aria-label="Card front">
    <div class="brand">
      <span class="brand-dot"></span>
      <div class="brand-name">Bluefern Trading<br>Partners, Ltd.</div>
    </div>
    <div class="divider"></div>
    <div class="contact">
      <div class="person">Daniel Okafor</div>
      <div class="role">President</div>
      <div class="address">742 Hollis St. - Suite 0830<br>New York, NY 10093</div>
      <div class="line">
        <svg class="icon" viewBox="0 0 16 16" aria-hidden="true"><path d="M4 1h2l1.5 3.5-1.8 1.2a8 8 0 0 0 4.6 4.6l1.2-1.8L15 10v2a2 2 0 0 1-2 2C6.9 14 2 9.1 2 3a2 2 0 0 1 2-2z"/></svg>
        <span>212-555-0147 Ext-305</span>
      </div>
      <div class="line">
        <svg class="icon" viewBox="0 0 16 16" aria-hidden="true"><rect x="2" y="5" width="12" height="8" rx="1"/><rect x="4" y="1" width="8" height="4"/></svg>
        <span>212-555-0163</span>
      </div>
      <div class="plain">sales@bluefernexample.com</div>
    </div>
    <div class="web">www.bluefernexample.com</div>
  </section>
</main>
</body>
</html>
```